New Labels for VANTO Sports Drinks

Sports drink company looking for new fresh look with commercial appeal beverage labels. You can use the current label as a guide but adjust where you see fit. Would like to standout from other sports drink on store shelves. VANTO Sports Drinks is a fusion of real brewed tea and all natural electrolytes. Our tea features a bold, full-bodied flavor profile, combined with all natural electrolytes, giving you one of the very first tea based sports drinks.

Target Market(s)

16-40

Colors

Designer to choose colors to be used in the design.

Requirements
Must have
• Name
• flavor
• description
• nutritional info
• all Info on back of labels
Nice to have
• sports image
• fruit flavor
• white background
• Real tea and natural electrolytes
Should not have
• n/a

```html
<!DOCTYPE html>
<html lang="en">
<head>
<meta charset="utf-8">
<title>VANTO Sports Drinks – Label Range</title>
<link href="https://fonts.googleapis.com/css2?family=Archivo+Black&family=Raleway:wght@300;400;700&display=swap" rel="stylesheet">
<style>
  :root {
    --bg: #ffffff;
    --label-white: #ffffff;
    --label-black: #0b0b0b;
    --tea-green: #8cc63f;
    --deep-green: #14622e;
    --lemon: #f2e600;
    --pineapple: #f07f22;
    --aqua: #16b3c4;
    --navy: #1a4f8a;
    --silver: #a9abae;
    --ink: #1d3b24;
  }
  * { box-sizing: border-box; margin: 0; padding: 0; }
  html, body { width: 1200px; height: 1200px; overflow: hidden; background: var(--bg); }
  .range { position: relative; width: 1200px; height: 1200px; }

  .label {
    position: absolute;
    font-size: 10px;
    width: 18.2em;
    height: 23.4em;
    background: linear-gradient(90deg, #e4e4e4 0%, var(--label-white) 14%, var(--label-white) 86%, #e4e4e4 100%);
    display: flex;
    flex-direction: column;
    align-items: center;
    padding-top: 2.2em;
    font-family: "Raleway", sans-serif;
    --accent: var(--lemon);
    --tag: var(--tea-green);
  }
  .label--lemon { left: 186px; top: 272px; }
  .label--black { left: 497px; top: 272px; --accent: #ffffff;
    background: linear-gradient(90deg, #3a3a3a 0%, var(--label-black) 14%, var(--label-black) 86%, #3a3a3a 100%); }
  .label--pineapple { left: 778px; top: 270px; --accent: var(--pineapple); }
  .label--unsweetened { left: 186px; top: 824px; --accent: var(--deep-green); }
  .label--water { left: 456px; top: 824px; --accent: var(--aqua); --tag: var(--navy); }
  .label--feature { left: 756px; top: 686px; font-size: 18.8px; --accent: var(--silver); }

  .brand { display: flex; align-items: flex-start; gap: 0.4em; }
  .brand__name {
    font-family: "Archivo Black", sans-serif;
    font-size: 3.5em;
    line-height: 1;
    letter-spacing: -0.02em;
    color: var(--accent);
  }
  .brand__tag {
    writing-mode: vertical-rl;
    font-size: 1.6em;
    font-weight: 300;
    color: var(--tag);
    line-height: 1;
  }
  .flavor {
    margin-top: 0.8em;
    font-size: 2.6em;
    font-weight: 300;
    letter-spacing: -0.04em;
    line-height: 1;
    color: var(--flavor, var(--accent));
  }
  .label--lemon .flavor, .label--feature .flavor { --flavor: var(--lemon); }
  .label--unsweetened .flavor { font-size: 1.9em; }
  .label--black .flavor, .label--water .flavor { font-size: 2.2em; }
  .desc {
    margin-top: 0.3em;
    font-size: 1.6em;
    font-weight: 300;
    color: var(--tag);
    letter-spacing: -0.02em;
  }
  .mark {
    margin-top: 1em;
    width: 4.4em;
    height: 4.4em;
    border-radius: 50%;
    background: var(--accent);
  }
  .label--black .mark { background: var(--deep-green); }
  .label--feature .mark { background: var(--silver); }
  .volume {
    margin-top: auto;
    margin-bottom: 1.4em;
    font-size: 0.78em;
    font-weight: 700;
    color: var(--ink);
  }
  .label--black .volume { color: var(--deep-green); }
</style>
</head>
<body>
<main class="range">

  <section class="label label--lemon">
    <div class="brand"><span class="brand__name">VANTO</span><span class="brand__tag">sports tea</span></div>
    <p class="flavor">LEMON</p>
    <p class="desc">tea+electrolytes</p>
    <div class="mark"></div>
    <p class="volume">16FL.OZ.(474ML)</p>
  </section>

  <section class="label label--black">
    <div class="brand"><span class="brand__name">VANTO</span><span class="brand__tag">sports tea</span></div>
    <p class="flavor">BLACK TEA</p>
    <p class="desc">tea+electrolytes</p>
    <div class="mark"></div>
    <p class="volume">16FL.OZ.(474ML)</p>
  </section>

  <section class="label label--pineapple">
    <div class="brand"><span class="brand__name">VANTO</span><span class="brand__tag">sports tea</span></div>
    <p class="flavor">PINEAPPLE</p>
    <p class="desc">tea+electrolytes</p>
    <div class="mark"></div>
    <p class="volume">16FL.OZ.(474ML)</p>
  </section>

  <section class="label label--unsweetened">
    <div class="brand"><span class="brand__name">VANTO</span><span class="brand__tag">sports tea</span></div>
    <p class="flavor">UNSWEETENED</p>
    <p class="desc">tea+electrolytes</p>
    <div class="mark"></div>
    <p class="volume">16FL.OZ.(474ML)</p>
  </section>

  <section class="label label--water">
    <div class="brand"><span class="brand__name">VANTO</span><span class="brand__tag">sports water</span></div>
    <p class="flavor">POWER H2O</p>
    <p class="desc">water+electrolytes</p>
    <div class="mark"></div>
    <p class="volume">16FL.OZ.(474ML)</p>
  </section>

  <section class="label label--feature">
    <div class="brand"><span class="brand__name">VANTO</span><span class="brand__tag">sports tea</span></div>
    <p class="flavor">LEMON</p>
    <p class="desc">tea+electrolytes</p>
    <div class="mark"></div>
    <p class="volume">16FL.OZ.(474ML)</p>
  </section>

</main>
</body>
</html>
```